A social health network MOBILE APP needs an awesome home page

We need a home page design that is attractive, and simple to navigate for our mobile app. This app helps people maintain their personal health records, find and connect with care providers to ask question, get care online or face to face through appointment. It also has a few other features to encourage engagement such as Forum, Reward, Service Discount Coupon.
We would like to see the design that uses the color green (our company color) as the main color, and includes an area for announcement plus another area for advertising. We include sketches of our need for your review.
The final design should look modern, friendly, and lively.
Updates
If possible, please break away from our attached sketch format and let your creativity leads the way? We would like to see the bottom buttons layout in differently from the sketch.
Industry/Entity Type
Health
Colors
Designer to choose colors to be used in the design.
Requirements
Must have
- A clean and elegant look.

```html
<!DOCTYPE html>
<html lang="en">
<head>
<meta charset="utf-8">
<title>Health Network App – Home Screens</title>
<link href="https://fonts.googleapis.com/css2?family=Roboto:wght@400;500;700&display=swap" rel="stylesheet">
<style>
  :root{
    --canvas:#dcdcdc;
    --green:#1fae49;
    --green-dark:#17963b;
    --green-band:rgba(60,190,90,.72);
    --blue:#3657ac;
    --tile-ink:#e4e6ee;
    --circle:#ececec;
    --nav:#0f1010;
    --nav-ink:#b9b9b9;
    --orange:#e48a23;
    --brand-red:#d9261c;
    --gap:#eceff3;
  }
  *{box-sizing:border-box;margin:0;padding:0}
  html,body{width:1200px;height:1200px;overflow:hidden;background:var(--canvas);font-family:"Roboto",Arial,sans-serif}
  .canvas{position:relative;width:1200px;height:1200px;overflow:hidden}
  .screen{position:absolute;width:459px;background:var(--gap)}
  .screen--home{left:61px;top:288px;height:912px}
  .screen--menu{left:615px;top:6px;height:731px}

  .status-bar{position:absolute;left:0;top:0;width:100%;height:26px;background:var(--green);color:#fff;font-size:13px;font-weight:500;display:flex;align-items:center;justify-content:space-between;padding:0 12px}
  .status-bar__left,.status-bar__right{display:flex;align-items:center;gap:5px}
  .battery{width:26px;height:11px;border:1.5px solid #fff;border-radius:3px;padding:1px}
  .battery span{display:block;width:90%;height:100%;background:#fff;border-radius:1px}

  .hero{position:absolute;left:0;top:26px;width:100%;height:241px;background:linear-gradient(120deg,#7a5a3a 0%,#c9a17a 35%,#efe6dc 55%,#8f7260 80%,#5b4a3e 100%)}
  .hero__caption{position:absolute;left:0;top:186px;width:100%;height:55px;background:var(--green-band);color:#fff;font-size:22px;line-height:21px;text-align:center;padding-top:7px}
  .pager{position:absolute;left:0;top:267px;width:100%;height:26px;background:var(--green-dark);display:flex;justify-content:center;align-items:center;gap:18px}
  .pager i{width:10px;height:10px;border-radius:50%;background:#fff}
  .pager i.is-active{background:#111}

  .quick-actions{position:absolute;left:0;top:293px;width:100%;height:169px;background:var(--green)}
  .quick-action{position:absolute;top:0;width:140px;margin-left:-70px;text-align:center;color:#fff;font-weight:700;font-size:14.5px}
  .quick-action__circle{width:83px;height:83px;margin:39px auto 0;border-radius:50%;background:var(--circle);display:flex;align-items:center;justify-content:center}
  .quick-action__label{margin-top:21px}

  .feature-grid{position:absolute;left:0;width:100%;height:404px;background:var(--blue)}
  .screen--home .feature-grid{top:468px}
  .screen--menu .feature-grid{top:0}
  .feature{position:absolute;width:150px;margin-left:-75px;text-align:center;color:var(--tile-ink);font-size:17.5px}
  .feature svg{display:block;margin:0 auto 4px;width:60px;height:60px}

  .promo{position:absolute;left:0;width:100%;background:linear-gradient(115deg,#7fa46a 0%,#c7b9a4 35%,#e4d2c2 55%,#a9b38e 75%,#6f8d58 100%);overflow:hidden}
  .screen--home .promo{top:875px;height:37px}
  .screen--menu .promo{top:407px;height:255px}
  .promo__brand{position:absolute;left:10px;top:12px;color:var(--brand-red);font-weight:700;font-size:24px;letter-spacing:-.5px}
  .screen--home .promo__brand{top:8px;font-size:22px}
  .promo__tagline{position:absolute;left:126px;top:20px;color:#fff;font-size:8.5px;letter-spacing:.5px;opacity:.85}
  .screen--home .promo__tagline{left:128px;top:16px}
  .promo__offer{position:absolute;right:0;bottom:0;width:175px;height:205px;background:var(--orange);clip-path:polygon(100% 0,100% 100%,0 100%)}
  .promo__discount{position:absolute;right:20px;top:143px;color:#fff;font-size:36px;font-weight:400}
  .promo__note{position:absolute;right:20px;top:183px;width:90px;text-align:center;color:#fff;font-size:7.5px;line-height:10px}
  .promo__badge{position:absolute;right:22px;top:220px;width:58px;height:24px;border-radius:4px;background:rgba(255,255,255,.85)}
  .promo__dots{position:absolute;left:216px;top:233px;display:flex;gap:10px}
  .promo__dots i{width:8px;height:8px;border-radius:50%;background:rgba(255,255,255,.8)}
  .promo__dots i.is-active{background:#29b34a}
  .promo__progress{position:absolute;left:0;bottom:0;width:92px;height:3px;background:#fff}

  .tab-bar{position:absolute;left:0;top:666px;width:100%;height:65px;background:var(--nav)}
  .tab{position:absolute;top:0;width:92px;margin-left:-46px;text-align:center;color:var(--nav-ink);font-size:13px}
  .tab svg{display:block;margin:8px auto 3px;width:32px;height:32px}
  .tab.is-active{color:#fff}
</style>
</head>
<body>
<div class="canvas">

  <!-- Home screen -->
  <section class="screen screen--home">
    <div class="status-bar">
      <div class="status-bar__left">
        <svg width="14" height="10" viewBox="0 0 14 10"><rect x="0" y="7" width="2" height="3" fill="#fff"/><rect x="4" y="5" width="2" height="5" fill="#fff"/><rect x="8" y="3" width="2" height="7" fill="#9be3a8"/><rect x="12" y="0" width="2" height="10" fill="#9be3a8"/></svg>
        <span>Nova Wi-Fi</span>
        <svg width="16" height="12" viewBox="0 0 16 12"><path d="M1 4a10 10 0 0 1 14 0M3.5 6.5a6.5 6.5 0 0 1 9 0M6 9a3 3 0 0 1 4 0" stroke="#fff" stroke-width="1.8" fill="none" stroke-linecap="round"/></svg>
      </div>
      <span>9:54 AM</span>
      <div class="status-bar__right">
        <svg width="8" height="12" viewBox="0 0 8 12"><path d="M1 3l6 5-3 3V1l3 3-6 5" stroke="#fff" stroke-width="1.3" fill="none"/></svg>
        <span>91%</span>
        <div class="battery"><span></span></div>
      </div>
    </div>

    <div class="hero" role="img" aria-label="Photo of a smiling woman checking her phone on a busy street">
      <p class="hero__caption">In just few seconds you can<br>get results</p>
    </div>
    <div class="pager"><i class="is-active"></i><i></i><i></i><i></i><i></i></div>

    <div class="quick-actions">
      <div class="quick-action" style="left:83px">
        <div class="quick-action__circle">
          <svg width="36" height="40" viewBox="0 0 36 40"><rect x="2" y="5" width="32" height="34" rx="3" fill="#1fae49"/><rect x="12" y="1" width="12" height="8" rx="2" fill="#1fae49" stroke="#ececec" stroke-width="2"/><path d="M10 23l6 6 11-12" stroke="#fff" stroke-width="3.5" fill="none" stroke-linecap="round" stroke-linejoin="round"/></svg>
        </div>
        <p class="quick-action__label">Records</p>
      </div>
      <div class="quick-action" style="left:230px">
        <div class="quick-action__circle">
          <svg width="50" height="40" viewBox="0 0 50 40"><path d="M12 30a10 10 0 0 1 0-20 14 14 0 0 1 26 2 9 9 0 0 1 0 18z" fill="#1fae49"/><path d="M20 15a5 5 0 1 1 7 4.5c-1.5.8-2 1.6-2 3.5" stroke="#ececec" stroke-width="3.5" fill="none" stroke-linecap="round"/><circle cx="25" cy="34" r="3.2" fill="none" stroke="#1fae49" stroke-width="2.5"/></svg>
        </div>
        <p class="quick-action__label">Questions</p>
      </div>
      <div class="quick-action" style="left:378px">
        <div class="quick-action__circle">
          <svg width="30" height="40" viewBox="0 0 30 40"><path d="M15 39C5 26 2 20 2 14a13 13 0 0 1 26 0c0 6-3 12-13 25z" fill="#1fae49"/><circle cx="15" cy="14" r="5" fill="#ececec"/></svg>
        </div>
        <p class="quick-action__label">Find service</p>
      </div>
    </div>

    <div class="feature-grid">
      <div class="feature" style="left:95px;top:50px">
        <svg viewBox="0 0 60 60"><path d="M4 6h36v26H16l-8 8v-8H4z" fill="var(--tile-ink)"/><path d="M44 16h12v30h-4v8l-8-8H20v-10h24z" fill="var(--tile-ink)"/></svg>Forum</div>
      <div class="feature" style="left:241px;top:50px">
        <svg viewBox="0 0 60 60" fill="none" stroke="var(--tile-ink)" stroke-width="5"><circle cx="30" cy="14" r="9"/><circle cx="13" cy="44" r="9"/><circle cx="47" cy="44" r="9"/><path d="M25 22l-8 14M35 22l8 14M22 44h16"/></svg>Connections</div>
      <div class="feature" style="left:389px;top:50px">
        <svg viewBox="0 0 60 60"><circle cx="26" cy="16" r="13" fill="var(--tile-ink)"/><path d="M2 56c0-17 9-25 24-25 6 0 11 1 15 4v21z" fill="var(--tile-ink)"/><path d="M49 38v18M40 47h18" stroke="var(--tile-ink)" stroke-width="4"/></svg>Invite</div>
      <div class="feature" style="left:95px;top:183px">
        <svg viewBox="0 0 60 60"><path d="M18 4h24l-4 9H22z" fill="var(--tile-ink)"/><path d="M20 15h20c12 8 18 20 16 32-1 6-6 9-12 9H16c-6 0-11-3-12-9-2-12 4-24 16-32z" fill="var(--tile-ink)"/><text x="30" y="47" font-size="24" font-weight="700" text-anchor="middle" fill="var(--blue)" font-family="Roboto,sans-serif">$</text></svg>Rewards</div>
      <div class="feature" style="left:241px;top:183px">
        <svg viewBox="0 0 60 60" fill="none" stroke="var(--tile-ink)" stroke-width="4"><rect x="18" y="18" width="38" height="32" rx="4"/><rect x="25" y="25" width="24" height="18" stroke-dasharray="3 3" stroke-width="2.5"/><circle cx="9" cy="10" r="6"/><circle cx="9" cy="30" r="6"/><path d="M14 13l20 12M14 27l20-12"/></svg>Coupons</div>
      <div class="feature" style="left:389px;top:183px">
        <svg viewBox="0 0 60 60" fill="none" stroke="var(--tile-ink)" stroke-width="5"><path d="M4 18V4h14M42 4h14v14M56 42v14H42M18 56H4V42"/><path d="M18 20v20M28 22v6M28 34v6M40 20v20" stroke-width="5"/></svg>Scan Voucher</div>
      <div class="feature" style="left:241px;top:300px">
        <svg viewBox="0 0 60 60"><path d="M30 3a27 27 0 0 1 9 52l-9 5-9-5A27 27 0 0 1 30 3z" fill="none" stroke="var(--tile-ink)" stroke-width="4"/><circle cx="30" cy="17" r="4" fill="var(--tile-ink)"/><path d="M24 25h9v18h4M24 43h13" stroke="var(--tile-ink)" stroke-width="5" fill="none"/></svg>Info</div>
    </div>

    <div class="promo" role="img" aria-label="Advertisement photo of a grandparent family playing outdoors">
      <span class="promo__brand">Vita Blend</span>
      <span class="promo__tagline">ULTRA PREMIUM NUTRITIONAL SHAKE MIX</span>
    </div>
  </section>

  <!-- Menu screen -->
  <section class="screen screen--menu">
    <div class="feature-grid">
      <div class="feature" style="left:83px;top:50px">
        <svg viewBox="0 0 60 60"><path d="M4 6h36v26H16l-8 8v-8H4z" fill="var(--tile-ink)"/><path d="M44 16h12v30h-4v8l-8-8H20v-10h24z" fill="var(--tile-ink)"/></svg>Forum</div>
      <div class="feature" style="left:229px;top:50px">
        <svg viewBox="0 0 60 60" fill="none" stroke="var(--tile-ink)" stroke-width="5"><circle cx="30" cy="14" r="9"/><circle cx="13" cy="44" r="9"/><circle cx="47" cy="44" r="9"/><path d="M25 22l-8 14M35 22l8 14M22 44h16"/></svg>Connections</div>
      <div class="feature" style="left:377px;top:50px">
        <svg viewBox="0 0 60 60"><circle cx="26" cy="16" r="13" fill="var(--tile-ink)"/><path d="M2 56c0-17 9-25 24-25 6 0 11 1 15 4v21z" fill="var(--tile-ink)"/><path d="M49 38v18M40 47h18" stroke="var(--tile-ink)" stroke-width="4"/></svg>Invite</div>
      <div class="feature" style="left:83px;top:180px">
        <svg viewBox="0 0 60 60"><path d="M18 4h24l-4 9H22z" fill="var(--tile-ink)"/><path d="M20 15h20c12 8 18 20 16 32-1 6-6 9-12 9H16c-6 0-11-3-12-9-2-12 4-24 16-32z" fill="var(--tile-ink)"/><text x="30" y="47" font-size="24" font-weight="700" text-anchor="middle" fill="var(--blue)" font-family="Roboto,sans-serif">$</text></svg>Rewards</div>
      <div class="feature" style="left:229px;top:180px">
        <svg viewBox="0 0 60 60" fill="none" stroke="var(--tile-ink)" stroke-width="4"><rect x="18" y="18" width="38" height="32" rx="4"/><rect x="25" y="25" width="24" height="18" stroke-dasharray="3 3" stroke-width="2.5"/><circle cx="9" cy="10" r="6"/><circle cx="9" cy="30" r="6"/><path d="M14 13l20 12M14 27l20-12"/></svg>Coupons</div>
      <div class="feature" style="left:377px;top:180px">
        <svg viewBox="0 0 60 60" fill="none" stroke="var(--tile-ink)" stroke-width="5"><path d="M4 18V4h14M42 4h14v14M56 42v14H42M18 56H4V42"/><path d="M18 20v20M28 22v6M28 34v6M40 20v20"/></svg>Scan Voucher</div>
      <div class="feature" style="left:234px;top:297px">
        <svg viewBox="0 0 60 60"><path d="M30 3a27 27 0 0 1 9 52l-9 5-9-5A27 27 0 0 1 30 3z" fill="none" stroke="var(--tile-ink)" stroke-width="4"/><circle cx="30" cy="17" r="4" fill="var(--tile-ink)"/><path d="M24 25h9v18h4M24 43h13" stroke="var(--tile-ink)" stroke-width="5" fill="none"/></svg>Info</div>
    </div>

    <div class="promo" role="img" aria-label="Advertisement photo of grandparents playing with their granddaughter, with shake mix products">
      <span class="promo__brand">Vita Blend</span>
      <span class="promo__tagline">ULTRA PREMIUM NUTRITIONAL SHAKE MIX</span>
      <div class="promo__offer"></div>
      <span class="promo__discount">-25%</span>
      <span class="promo__note">+ Free shipping to Vietnam &amp; within the USA continent</span>
      <div class="promo__badge"></div>
      <div class="promo__dots"><i></i><i></i><i class="is-active"></i></div>
      <div class="promo__progress"></div>
    </div>

    <nav class="tab-bar">
      <div class="tab is-active" style="left:46px">
        <svg viewBox="0 0 32 32"><path d="M4 15L16 4l12 11v14H4z" fill="none" stroke="#fff" stroke-width="3.2" stroke-linejoin="round"/></svg>Home</div>
      <div class="tab" style="left:137px">
        <svg viewBox="0 0 32 32" fill="none" stroke="var(--nav-ink)" stroke-width="3.5"><circle cx="7" cy="25" r="3" fill="var(--nav-ink)" stroke="none"/><path d="M4 15a13 13 0 0 1 13 13M4 7a21 21 0 0 1 21 21"/></svg>Feed</div>
      <div class="tab" style="left:229px">
        <svg viewBox="0 0 32 32" fill="none" stroke="var(--nav-ink)" stroke-width="2.5"><path d="M8 22V14a8 8 0 0 1 16 0v8l3 3H5z"/><path d="M13 28a3 3 0 0 0 6 0M16 3v3"/></svg>Notification</div>
      <div class="tab" style="left:321px">
        <svg viewBox="0 0 32 32" fill="none" stroke="var(--nav-ink)" stroke-width="2.5"><rect x="3" y="7" width="26" height="18" rx="1"/><path d="M3 8l13 10 13-10"/></svg>Message</div>
      <div class="tab" style="left:413px">
        <svg viewBox="0 0 32 32" fill="none" stroke="var(--nav-ink)" stroke-width="2.2"><circle cx="16" cy="16" r="4.5"/><path d="M16 3l2.5 3.5 4-1.5 1 4.2 4.2 1-1.5 4 3.5 2.5-3.5 2.5 1.5 4-4.2 1-1 4.2-4-1.5L16 29l-2.5-3.5-4 1.5-1-4.2-4.2-1 1.5-4L2.3 16l3.5-2.5-1.5-4 4.2-1 1-4.2 4 1.5z"/></svg>Settings</div>
    </nav>
  </section>

</div>
</body>
</html>
```